Business Card needed for Drainor, a growing Septic Service company

Drainor, a growing local septic service company in Pennsylvania, needs updated business cards. We'd like the business card to feature our logo and communicate that we provide Septic Pumping, Installations/Repairs, Restroom Rentals, and 24/7 Emergency Service. The business card should be eye-catching, bold, and clean/simple. We have been in business almost 10 years and would like to expand and update our business brand and image.

Target Market(s)

Residential and Commercial, New and Current Homeowners

Industry/Entity Type

Service

Contact Information for Business Card

Contact on the business card should be: Dean Harlow Owner & Operator
Phone: 610-555-0187
Email: service@drainor-example.com
Website: www.drainor-example.com
Address: 812 Millbrook Lane Easton PA 18042

Font styles to use
Sans Serif

Colors

Designer to choose colors to be used in the design.

Requirements
Must have
• Feature logo on both side of business card.
Nice to have
• We envision the contact information on one side and our services listed on the other side. Utilize the green from the symbol in our logo as part of the design, overall design color scheme should be white, grey, black.

```html
<!DOCTYPE html>
<html lang="en">
<head>
<meta charset="utf-8">
<title>Drainor Business Card</title>
<link rel="stylesheet" href="https://fonts.googleapis.com/css2?family=Open+Sans:wght@400;700;800&display=swap">
<style>
  :root {
    --backdrop: #e3e3e3;
    --card: #f4f4f4;
    --green: #82bc3f;
    --ink: #0d0d0d;
    --white: #ffffff;
  }
  * { margin: 0; padding: 0; box-sizing: border-box; }
  html, body { width: 1200px; height: 960px; overflow: hidden; }
  body {
    background: var(--backdrop);
    font-family: "Open Sans", sans-serif;
    position: relative;
  }
  .card {
    position: absolute;
    left: 306px;
    width: 585px;
    height: 335px;
    background: var(--card);
  }
  .card--front { top: 121px; }
  .card--back { top: 506px; }

  .brand {
    position: absolute;
    display: flex;
    align-items: center;
    font-weight: 800;
    color: var(--ink);
    letter-spacing: 2px;
    line-height: 1;
  }
  .brand--front { left: 109px; top: 129px; font-size: 58px; }
  .brand__square {
    width: 63px; height: 64px;
    background: var(--green);
    margin-right: 14px;
  }

  .services {
    position: absolute;
    left: 0; right: 0; top: 266px;
    text-align: center;
    font-size: 16px;
    color: var(--ink);
  }
  .services__dot {
    display: inline-block;
    width: 8px; height: 8px;
    border-radius: 50%;
    background: var(--green);
    margin: 0 4px 1px;
  }
  .emergency {
    position: absolute;
    left: 0; right: 0; top: 291px;
    text-align: center;
    font-size: 15px;
    font-weight: 700;
    color: var(--green);
    letter-spacing: 0.4px;
  }

  .panel {
    position: absolute;
    left: 26px; top: 21px;
    width: 537px; height: 292px;
    background: var(--green);
  }
  .brand--back { right: 28px; top: 32px; font-size: 40px; }

  .address, .contact {
    position: absolute;
    right: 28px;
    text-align: right;
    color: var(--white);
    font-size: 16px;
    line-height: 20px;
  }
  .address { top: 151px; }
  .contact { top: 207px; }
  .contact__row { display: flex; justify-content: flex-end; align-items: center; gap: 6px; }
  .contact__icon { width: 13px; height: 13px; fill: var(--ink); }

  .person { position: absolute; left: 39px; top: 223px; }
  .person__name { font-size: 20px; font-weight: 700; color: var(--white); line-height: 26px; }
  .person__role { font-size: 16px; color: var(--ink); line-height: 22px; }
</style>
</head>
<body>
  <section class="card card--front">
    <div class="brand brand--front"><span class="brand__square"></span>DRAINOR</div>
    <p class="services">Septic Pumping <span class="services__dot"></span> Installations/Repairs <span class="services__dot"></span> Restroom Rentals</p>
    <p class="emergency">24/7 EMERGENCY SERVICE</p>
  </section>

  <section class="card card--back">
    <div class="panel">
      <div class="brand brand--back">DRAINOR</div>
      <p class="address">812 Millbrook Lane<br>Alderwick PA 18000</p>
      <div class="contact">
        <p class="contact__row">610-555-0187
          <svg class="contact__icon" viewBox="0 0 24 24"><path d="M6.6 10.8a15 15 0 0 0 6.6 6.6l2.2-2.2a1 1 0 0 1 1-.25 11.4 11.4 0 0 0 3.6.6 1 1 0 0 1 1 1V20a1 1 0 0 1-1 1A17 17 0 0 1 3 4a1 1 0 0 1 1-1h3.5a1 1 0 0 1 1 1c0 1.25.2 2.45.6 3.6a1 1 0 0 1-.25 1z"/></svg></p>
        <p class="contact__row">service@drainor-example.com
          <svg class="contact__icon" viewBox="0 0 24 24"><path d="M2 5h20v14H2zm2 2v.5l8 5 8-5V7zm0 2.8V17h16V9.8l-8 5z"/></svg></p>
        <p class="contact__row">www.drainor-example.com
          <svg class="contact__icon" viewBox="0 0 24 24"><path d="M12 2a10 10 0 1 0 0 20 10 10 0 0 0 0-20zm7.9 9h-3.4a15 15 0 0 0-1.4-6.1A8 8 0 0 1 19.9 11zM12 4.1c.9 1.2 2.2 3.6 2.5 6.9h-5c.3-3.3 1.6-5.7 2.5-6.9zM4.1 13h3.4a15 15 0 0 0 1.4 6.1A8 8 0 0 1 4.1 13zm3.4-2H4.1a8 8 0 0 1 4.8-6.1A15 15 0 0 0 7.5 11zM12 19.9c-.9-1.2-2.2-3.6-2.5-6.9h5c-.3 3.3-1.6 5.7-2.5 6.9zm3.1-.8a15 15 0 0 0 1.4-6.1h3.4a8 8 0 0 1-4.8 6.1z"/></svg></p>
      </div>
      <div class="person">
        <p class="person__name">DEAN HARLOW</p>
        <p class="person__role">Owner &amp; Operator</p>
      </div>
    </div>
  </section>
</body>
</html>
```